Corrimal Lodge Web Design Project

I am looking for a striking, modern and user friendly site to promote my business, Corrimal Lodge.

Corrimal Lodge comprises of 3 elements : Restaurant, Resort and Events and the site must showcase all of these.
Updates

Project Deadline Extended
Reason: Too far away from brief ! Please check out the 2 website links to restaurant sites i LOVE for inspiration ! I am happy to pay for a quality designer and also for anyone that can code this !

Target Market(s)

Our Restaurant clientele demographic is 30-60 years old and are a mix of locals and tourists. The Restaurant is very much a destination venue so we attract people that wish to seek out amazing food.

The Event side of things attracts mainly weddings, this is a lucrative arm of the business and this side of the site must also be outstanding.

The Resort comprises of 7 boutique loft apartment and has a big pool and spa. We attract a mix of locals but want to push it as a ' getaway '

Industry/Entity Type

Business

Requirements
Must have
• I would like the first page to be an overall blog and to highlight the 3 area of the business. Lets have the 3 keywords as clickable tabs that take you to that section of the site.

RESTAURANT RESORT EVENTS

The RESTAURANT page should include the following tabs ( i have provided the information to be added to each tab as an example )

MENU ( Breakfast, Lunch, Dinner, Set Menu, Wine List)

FUNCTIONS (Private Dining Room, Exclusive Use, Wine Nights Coming Soon)

RESERVATIONS (Enquiry Form linked to my info@ address, Reservation Policies, Contact Number)

GALLERY & PRESS ( Press Articles, Latest News, What's On, Photo's, Wedding Hot Spot)

CONTACT US (Opening Times, Map, Contact Details, Sign Up For Our Newsletter, Chatterbook Link )

The RESORT page should include the following tabs :
# LOFTS & RATES
# FACILITIES
# SPECIAL OFFERS
# GALLERY
# RESERVATIONS

The EVENTS page should include the following tabs :
# WEDDINGS
# CONFERENCES
# PRIVATE EVENTS
# GALLERY
# ENQUIRY FORM
Nice to have
• Include Logo, good branding

```html
<!DOCTYPE html>
<html lang="en">
<head>
<meta charset="utf-8">
<title>Corrimal Lodge</title>
<link rel="stylesheet" href="https://fonts.googleapis.com/css2?family=Almendra+SC&family=Gelasio:wght@400;700&display=swap">
<style>
  :root {
    --ochre-deep: #b06f22;
    --ochre: #d89a45;
    --parchment: #ece6b8;
    --parchment-light: #f1ecc6;
    --top-band: #9aa45a;
    --brown-dark: #3b2410;
    --brown: #6b4422;
    --brown-tab: #7a5230;
    --cream: #f3e6c8;
    --tile-frame: #050302;
    --white: #ffffff;
  }
  * { box-sizing: border-box; margin: 0; padding: 0; }
  html, body { width: 1200px; height: 710px; overflow: hidden; }
  body {
    position: relative;
    font-family: "Gelasio", Georgia, serif;
    color: var(--brown-dark);
    background:
      radial-gradient(ellipse 520px 420px at 50% 40%, var(--parchment-light) 0%, var(--parchment) 45%, rgba(236,230,184,0) 100%),
      radial-gradient(ellipse 760px 560px at 50% 50%, var(--ochre) 40%, var(--ochre-deep) 100%);
  }
  .top-band {
    position: absolute; left: 0; top: 0; width: 1200px; height: 43px;
    background: linear-gradient(90deg, #8c8f55, var(--top-band) 40%, #b3b56a 70%, #8e9a4e);
    box-shadow: 0 3px 8px rgba(60,40,10,.45);
  }
  .brand {
    position: absolute; left: 0; top: 68px; width: 1200px; text-align: center;
    color: var(--brown-dark);
  }
  .brand-welcome {
    font-family: "Gelasio", Georgia, serif; font-weight: 700;
    font-size: 26px; letter-spacing: 4px; line-height: 30px;
  }
  .brand-name {
    margin-top: 38px;
    font-family: "Gelasio", Georgia, serif; font-weight: 700;
    font-size: 52px; letter-spacing: 3px; line-height: 60px; text-transform: uppercase;
  }
  .sections { position: absolute; left: 189px; top: 255px; width: 821px; height: 176px; }
  .section-tile {
    position: absolute; top: 0; width: 265px; height: 176px;
    border: 6px solid var(--tile-frame); background: var(--tile-frame);
    display: block; text-decoration: none;
  }
  .section-tile .photo { position: absolute; inset: 0; }
  .section-tile .label {
    position: absolute; left: 0; right: 0; top: 72px; text-align: center;
    font-family: "Almendra SC", Georgia, serif; font-size: 30px; line-height: 32px;
    color: var(--white); text-shadow: 0 2px 4px rgba(0,0,0,.8);
  }
  .tile-restaurant { left: 0; }
  .tile-resort { left: 278px; }
  .tile-events { left: 556px; }
  .tile-restaurant .photo { background: radial-gradient(ellipse at 45% 55%, #5f7a2c 0%, #3a3a1c 45%, #1b1208 100%); }
  .tile-resort .photo { background: linear-gradient(180deg, #6a6458 0%, #4f4a3e 40%, #3d5a52 70%, #3a2620 100%); }
  .tile-events .photo { background: radial-gradient(ellipse at 50% 60%, #6d4a24 0%, #2c1f18 55%, #0e0b10 100%); }
  .press {
    position: absolute; left: 190px; top: 465px; width: 820px; height: 212px;
    border-radius: 10px;
    background: rgba(244,238,200,.55);
    box-shadow: 0 0 14px rgba(120,80,20,.35);
  }
  .press-tab {
    position: absolute; left: 531px; top: 447px; width: 150px; height: 32px;
    background: var(--brown-tab); color: var(--cream);
    font-weight: 700; font-size: 14px; letter-spacing: .5px;
    line-height: 32px; text-align: center;
  }
  .press-banner {
    position: absolute; left: 221px; top: 510px; width: 356px; height: 124px;
    border-radius: 8px;
    background: linear-gradient(160deg, rgba(150,100,50,.35), rgba(107,68,34,.5));
  }
  .press-story { position: absolute; left: 602px; top: 506px; width: 380px; color: var(--brown); }
  .press-kicker { font-weight: 700; font-size: 14px; line-height: 18px; text-transform: uppercase; }
  .press-headline { font-weight: 700; font-size: 19px; line-height: 24px; letter-spacing: .5px; text-transform: uppercase; }
  .press-lead { margin-top: 6px; font-weight: 700; font-size: 16px; line-height: 19px; color: var(--brown-dark); }
  .press-note { margin-top: 10px; font-size: 12px; line-height: 15px; color: var(--brown-dark); }
</style>
</head>
<body>
  <div class="top-band"></div>

  <header class="brand">
    <div class="brand-welcome">WELCOME</div>
    <div class="brand-name">Corrimal Lodge</div>
  </header>

  <nav class="sections">
    <a class="section-tile tile-restaurant" href="#restaurant">
      <div class="photo" role="img" aria-label="Photo of a fresh salad with glazed meat in a bowl"></div>
      <span class="label">RESTAURANT</span>
    </a>
    <a class="section-tile tile-resort" href="#resort">
      <div class="photo" role="img" aria-label="Photo of the resort pool deck with sun loungers and umbrellas"></div>
      <span class="label">RESORT</span>
    </a>
    <a class="section-tile tile-events" href="#events">
      <div class="photo" role="img" aria-label="Photo of the lodge veranda lit at dusk"></div>
      <span class="label">EVENTS</span>
    </a>
  </nav>

  <section class="press" aria-labelledby="press-title"></section>
  <h2 class="press-tab" id="press-title">IN THE PRESS</h2>
  <div class="press-banner" role="img" aria-label="Ribbon banner reading Extra Special Sunday"></div>
  <article class="press-story">
    <p class="press-kicker">Sundays at Corrimal Lodge just got</p>
    <p class="press-headline">Extra Special.</p>
    <p class="press-lead">Not only do we have our Sunday Roast, we also have all desserts available for $10.00.</p>
    <p class="press-note">Check out our new Dinner Menu (including our scrumptious desserts) located on our Chatterbook menu tab.</p>
  </article>
</body>
</html>
```